Roadwise Beacon Traffic Control Company Website

Modern website Wordpress design using all greyscale photos with a pop of red (such as road closure signs or detour cones) for strategic emphasis. (see brand guide for color codes)
The creative goal is to leverage high-contrast, desaturated imagery to create a clean, professional, and industrial feel. The selective use of red will draw immediate attention to critical elements—such as road hazards, safety equipment, or key messages to ensure the viewer's focus is directed with purpose.

Brand guide, homepage content and logo are attached. Create clean professional user experience to market services to industry professionals.

```html
<!DOCTYPE html>
<html lang="en">
<head>
<meta charset="utf-8">
<title>Roadwise Beacon Traffic Control</title>
<link href="https://fonts.googleapis.com/css2?family=Archivo:wght@400;500;600;700;800;900&family=Figtree:wght@400;500;600;700&display=swap" rel="stylesheet">
<style>
:root{
  --red:#e62129;
  --black:#000;
  --ink:#111;
  --grey:#777;
  --light:#f7f7f7;
  --white:#fff;
}
*{margin:0;padding:0;box-sizing:border-box}
html,body{width:1200px;height:2578px;overflow:hidden}
body{position:relative;background:var(--white);font-family:"Archivo",sans-serif;color:var(--ink)}
.abs{position:absolute}
.topline{left:0;top:0;width:1200px;height:6px;background:linear-gradient(90deg,var(--black) 50%,var(--red) 50%)}
.header{left:0;top:6px;width:1200px;height:111px;background:var(--white);box-shadow:0 3px 6px rgba(0,0,0,.25);z-index:2}
.brand{left:111px;top:24px;display:flex;align-items:center;gap:8px;font-size:18px;font-weight:800;line-height:1.1;color:var(--black);width:120px}
.brand .mark{width:14px;height:14px;background:var(--red);flex:none}
.nav{left:318px;top:43px;display:flex;font-size:15px;font-weight:500}
.nav a{color:var(--black);text-decoration:none;margin-right:41px;letter-spacing:.2px}
.nav a.active{color:var(--red)}
.quote{left:944px;top:33px;width:144px;height:47px;background:var(--black);color:var(--red);font-weight:600;font-size:15px;display:flex;align-items:center;justify-content:center}
.hero-bg{left:0;top:117px;width:1200px;height:548px;background:linear-gradient(100deg,#f2f2f2 0%,#dcdcdc 30%,#8a8a8a 45%,#5a5a5a 55%,#e2631a 65%,#f28a1c 78%,#3a3530 95%)}
.hero-fade{left:0;top:117px;width:620px;height:548px;background:linear-gradient(90deg,rgba(245,245,245,.95),rgba(245,245,245,.6) 75%,rgba(245,245,245,0))}
.hero-title{left:112px;top:186px;font-size:41px;font-weight:700;line-height:62px;color:var(--ink);width:460px}
.hero-sub{left:110px;top:435px;font-size:18px;font-weight:600;line-height:32px;width:320px}
.btn{background:var(--black);color:var(--white);font-weight:600;display:flex;align-items:center;justify-content:center}
.hero-btn{left:111px;top:513px;width:195px;height:63px;font-size:18px}
.notch{left:530px;top:623px}
.about-img{left:111px;top:786px;width:489px;height:403px;background:linear-gradient(160deg,#bfbfbf,#8f8f8f 45%,#e56a1e 60%,#3f3f3f 85%)}
.about-card{left:511px;top:901px;width:577px;height:462px;background:var(--white);box-shadow:0 4px 24px rgba(0,0,0,.18)}
.h2{font-size:52px;font-weight:900;letter-spacing:.5px;line-height:1}
.h2 span{color:var(--red)}
.kicker{font-size:15px;font-weight:700;letter-spacing:2px}
.accent-bar{width:60px;height:6px;background:var(--red)}
.about-title{left:599px;top:960px;font-size:44px}
.about-kicker{left:600px;top:1019px}
.about-bar{left:600px;top:1051px}
.about-text{left:598px;top:1080px;width:445px;font-size:14.5px;line-height:28.3px;color:var(--ink)}
.about-btn{left:600px;top:1264px;width:168px;height:51px;font-size:18px}
.services{left:0;top:1468px;width:1200px;height:705px;background:var(--light)}
.svc-title{left:0;top:1536px;width:1200px;text-align:center}
.svc-kicker{left:0;top:1594px;width:1200px;text-align:center}
.svc-bar{left:570px;top:1627px}
.svc-text{left:150px;top:1668px;width:900px;text-align:center;font-size:15px;line-height:31px}
.svc-img{top:1765px;width:312px;height:256px}
.svc-box{top:1948px;width:273px;height:140px;background:var(--white);box-shadow:0 6px 18px rgba(0,0,0,.08);padding:18px 20px;font-family:"Figtree",sans-serif}
.svc-box h3{font-size:18px;font-weight:600;color:var(--ink);margin-bottom:8px}
.svc-box p{font-size:15.5px;line-height:23px;color:var(--grey)}
.svc-box .more{font-family:"Archivo",sans-serif;font-size:14.5px;font-weight:700;color:var(--grey);margin-top:9px}
.arrow{top:1909px}
.footer{left:0;top:2173px;width:1200px;height:405px;background:var(--black)}
.foot-brand{left:72px;top:2320px;display:flex;align-items:center;gap:14px;font-size:34px;font-weight:800;color:var(--white);line-height:1.1;width:220px}
.foot-brand .mark{width:26px;height:26px;background:var(--red);flex:none}
.foot-head{left:320px;top:2262px;font-size:22px;font-weight:600;color:var(--white);font-family:"Figtree",sans-serif}
.links{top:2308px;list-style:none;font-size:15.5px;line-height:34.3px;color:var(--white);font-family:"Figtree",sans-serif}
.links li{display:flex;align-items:center;gap:8px}
.cert{left:935px;top:2308px;width:164px;height:125px;background:#eeefdd;border:3px solid #8fc7bf}
.rule{left:111px;top:2495px;width:977px;height:2px;background:#666}
.copy{left:0;top:2530px;width:1200px;text-align:center;font-size:16.5px;font-weight:700;color:var(--white);font-family:"Figtree",sans-serif}
</style>
</head>
<body>
<div class="abs topline"></div>
<header class="abs header">
  <div class="abs brand"><span class="mark"></span>Roadwise Beacon</div>
  <nav class="abs nav">
    <a class="active">HOME</a><a>ABOUT</a><a>SERVICES</a><a>RENTALS</a><a>JOBS</a><a>CONTACT</a>
  </nav>
  <div class="abs quote">GET A QUOTE</div>
</header>

<div class="abs hero-bg" role="img" aria-label="Greyscale roadside work zone with orange cones and a flagger warning sign"></div>
<div class="abs hero-fade"></div>
<h1 class="abs hero-title">TRAFFIC CONTROL SOLUTIONS ENGINEERED FOR SAFETY.</h1>
<p class="abs hero-sub">Safety Isn't A Priority, It's The Foundation Of Everything We Do</p>
<div class="abs btn hero-btn">GET STARTED</div>
<svg class="abs notch" width="140" height="44" viewBox="0 0 140 44">
  <path d="M0 44 C30 44 40 0 70 0 C100 0 110 44 140 44 Z" fill="#fff"/>
  <rect x="59" y="3" width="22" height="35" rx="11" fill="#8a8a8a"/>
  <path d="M70 12 V28 M64 23 L70 29 L76 23" stroke="#fff" stroke-width="2" fill="none"/>
</svg>

<div class="abs about-img" role="img" aria-label="Two orange traffic cones on an asphalt road in greyscale"></div>
<div class="abs about-card"></div>
<h2 class="abs h2 about-title">ABOUT <span>ROADWISE</span></h2>
<div class="abs kicker about-kicker">BEACON</div>
<div class="abs accent-bar about-bar"></div>
<p class="abs about-text">At Roadwise, safety isn’t just a priority—it’s our mission. As a leading traffic control company, we specialize in ensuring safe, efficient work zones for construction, infrastructure projects, and roadway maintenance. With a commitment to precision and reliability, we provide expert traffic management solutions that protect workers, motorists, and pedestrians alike.</p>
<div class="abs btn about-btn">READ MORE</div>

<section class="abs services"></section>
<h2 class="abs h2 svc-title">OUR <span>SERVICES</span></h2>
<div class="abs kicker svc-kicker">BEACON</div>
<div class="abs accent-bar svc-bar"></div>
<p class="abs svc-text">At Roadwise, we believe that every second counts when it comes to road safety. That’s why we use cutting-edge equipment, strategic planning, and highly trained personnel to minimize risk and maximize flow</p>

<div class="abs svc-img" style="left:87px;background:linear-gradient(160deg,#8d8d8d,#4e4e4e 55%,#c23a2c 80%,#777)" role="img" aria-label="Lane closure barrier with directional sign and work truck"></div>
<div class="abs svc-img" style="left:444px;background:linear-gradient(150deg,#9a9a9a,#555 50%,#e06a1e 75%,#888)" role="img" aria-label="Crew placing cones and barricades on a road"></div>
<div class="abs svc-img" style="left:792px;background:linear-gradient(160deg,#b5b5b5,#f04a1c 35%,#e8401a 80%,#c23a1a)" role="img" aria-label="Orange lane closed sign"></div>
<div class="abs svc-box" style="left:106px"><h3>Flagging &amp; Lane Closures</h3><p>Duis aute irure dolor in reprehend in voluptate velit</p><div class="more">READ MORE</div></div>
<div class="abs svc-box" style="left:463px"><h3>Signage &amp; Barricades</h3><p>Duis aute irure dolor in reprehend in voluptate velit</p><div class="more">READ MORE</div></div>
<div class="abs svc-box" style="left:811px"><h3>Roadway Detours &amp; Lane</h3><p>Duis aute irure dolor in reprehend in voluptate velit</p><div class="more">READ MORE</div></div>
<svg class="abs arrow" style="left:22px" width="38" height="38"><circle cx="19" cy="19" r="17" fill="#fff" stroke="#111" stroke-width="2"/><path d="M27 19H11 M17 13 L11 19 L17 25" stroke="#111" stroke-width="2" fill="none"/></svg>
<svg class="abs arrow" style="left:1128px" width="38" height="38"><circle cx="19" cy="19" r="17" fill="#fff" stroke="#111" stroke-width="2"/><path d="M11 19H27 M21 13 L27 19 L21 25" stroke="#111" stroke-width="2" fill="none"/></svg>

<footer class="abs footer"></footer>
<div class="abs foot-brand"><span class="mark"></span>Roadwise Beacon</div>
<div class="abs foot-head">Other Links</div>
<ul class="abs links" style="left:320px">
  <li><svg width="15" height="13"><path d="M1 6.5H13 M8 1.5 L13 6.5 L8 11.5" stroke="#fff" stroke-width="2.5" fill="none"/></svg>Road construction, maintenance, &amp; Detours</li>
  <li><svg width="15" height="13"><path d="M1 6.5H13 M8 1.5 L13 6.5 L8 11.5" stroke="#fff" stroke-width="2.5" fill="none"/></svg>Municipal &amp; State projects</li>
  <li><svg width="15" height="13"><path d="M1 6.5H13 M8 1.5 L13 6.5 L8 11.5" stroke="#fff" stroke-width="2.5" fill="none"/></svg>Private Sector &amp; Commercial Contractors</li>
  <li><svg width="15" height="13"><path d="M1 6.5H13 M8 1.5 L13 6.5 L8 11.5" stroke="#fff" stroke-width="2.5" fill="none"/></svg>Oil, Gas, Wind, Solar, &amp; Manufacturing</li>
</ul>
<ul class="abs links" style="left:671px">
  <li><svg width="15" height="13"><path d="M1 6.5H13 M8 1.5 L13 6.5 L8 11.5" stroke="#fff" stroke-width="2.5" fill="none"/></svg>State DOT-Compliant &amp; Certified</li>
  <li><svg width="15" height="13"><path d="M1 6.5H13 M8 1.5 L13 6.5 L8 11.5" stroke="#fff" stroke-width="2.5" fill="none"/></svg>Experienced &amp; Trained Crew</li>
  <li><svg width="15" height="13"><path d="M1 6.5H13 M8 1.5 L13 6.5 L8 11.5" stroke="#fff" stroke-width="2.5" fill="none"/></svg>Reliable &amp; Responsive</li>
  <li><svg width="15" height="13"><path d="M1 6.5H13 M8 1.5 L13 6.5 L8 11.5" stroke="#fff" stroke-width="2.5" fill="none"/></svg>Cost-Effective &amp; Efficient</li>
</ul>
<div class="abs cert" role="img" aria-label="Certification document"></div>
<div class="abs rule"></div>
<div class="abs copy">Copyrights@2025.Roadwise.All Rights Reserved</div>
</body>
</html>
```